Sri Lankan Cricket Tour For Girls Aged 14-18 in July 2018

We need a flyer to promote a cricket tour of Sri Lanka in July 2018 for girls aged 14-18.
We want the flyer to call for "expressions of interest".
We would like the Sri Lankan Flag also images of cricket ball and beaches and palm trees etc.
Mention Level 3 Coaches with International experience.
Target market is parents of girls aged 14 to 18 and girls aged 14 to 18

Target Market(s)

Parents of girls aged 14 to 18 and girls aged 14 to 18

Industry/Entity Type

Travel

Font styles to use
Serif
Sans Serif

Colors
0355a3
ec1f27
fbed22

Requirements
Must have
• Sri Lankan Flag, Halvey Athletics Logo, email address boyd@halveyathletics.com.au.
• - 10 Day Tour
• - Play on First Class Grounds
• - Level 3 Coaches With International Experience
• - For More Information Contact Boyd boyd@halveyathletics.com.au
Nice to have
• Picture of girls playing cricket, sun and beach
Should not have
• Cartoon type images
• Photo's of actual cricketers

```html
<!DOCTYPE html>
<html lang="en">
<head>
<meta charset="utf-8">
<title>Cricket Tour of Sri Lanka – Expressions of Interest</title>
<link rel="stylesheet" href="https://fonts.googleapis.com/css2?family=Questrial&family=Roboto+Condensed:ital,wght@0,300;0,400;1,700&family=Open+Sans:wght@400&family=Roboto:ital,wght@1,700&display=swap">
<style>
  :root {
    --page-bg: #0c5874;
    --sky-top: #0d2f7a;
    --sky-mid: #2a6fc4;
    --sky-low: #8fb7e0;
    --grass-top: #4f8a34;
    --grass-bottom: #1f4a1c;
    --white: #ffffff;
    --lime: #a8e824;
    --lime-soft: #c8f01e;
    --yellow: #f2f21a;
    --flag-gold: #ffbe29;
    --flag-green: #00834a;
    --flag-orange: #ff7a00;
    --flag-maroon: #8d1b3d;
    --brand-blue: #0355a3;
    --brand-red: #ec1f27;
  }
  * { margin: 0; padding: 0; box-sizing: border-box; }
  html, body { width: 1200px; height: 1198px; overflow: hidden; background: var(--page-bg); }
  .flyer {
    position: absolute; left: 210px; top: 42px; width: 780px; height: 1114px;
    overflow: hidden; color: var(--white);
    font-family: "Roboto Condensed", sans-serif;
  }
  .scene-photo {
    position: absolute; inset: 0;
    background: linear-gradient(180deg, var(--sky-top) 0%, var(--sky-mid) 35%, var(--sky-low) 62%, var(--grass-top) 66%, var(--grass-bottom) 100%);
  }
  .player-photo {
    position: absolute; left: 494px; top: 283px; width: 266px; height: 688px;
    border-radius: 120px 120px 30px 30px;
    background: linear-gradient(180deg, #4d6e7c 0%, #5a7a86 40%, #e9ecef 55%, #dfe3e6 90%, #2b2b2b 100%);
    opacity: .85;
  }
  .headline { position: absolute; left: 0; right: 0; top: 30px; text-align: center; font-family: "Questrial", sans-serif; }
  .headline .eoi { font-size: 52px; line-height: 62px; }
  .headline .tour { font-size: 46px; line-height: 62px; }
  .headline .tour em { font-family: "Roboto", sans-serif; font-style: italic; font-weight: 700; font-size: 58px; color: var(--lime); }
  .headline .ages { font-size: 46px; line-height: 58px; }
  .duration { position: absolute; left: 39px; top: 278px; }
  .duration .count { position: absolute; left: 0; top: 0; font-family: "Questrial", sans-serif; font-size: 112px; line-height: 112px; }
  .duration .label { position: absolute; left: 133px; top: 12px; white-space: nowrap; font-family: "Roboto", sans-serif; font-style: italic; font-weight: 700; font-size: 44px; color: var(--yellow); }
  .duration .dates { position: absolute; left: 124px; top: 70px; white-space: nowrap; font-family: "Open Sans", sans-serif; font-size: 28px; }
  .grounds { position: absolute; left: 48px; top: 410px; font-size: 44px; font-weight: 300; color: var(--lime-soft); }
  .flag { position: absolute; left: 92px; top: 485px; width: 304px; height: 158px; }
  .brand { position: absolute; left: 40px; width: 400px; top: 760px; text-align: center; }
  .brand .mark { width: 30px; height: 30px; border-radius: 50%; background: var(--brand-blue); display: inline-block; vertical-align: middle; margin-right: 10px; }
  .brand .name { font-size: 34px; font-weight: 400; color: var(--white); vertical-align: middle; }
  .coaches { position: absolute; left: 0; right: 0; top: 1010px; text-align: center; font-size: 34px; font-weight: 300; color: var(--lime-soft); }
  .contact { position: absolute; left: 0; right: 0; top: 1056px; text-align: center; font-size: 30px; font-weight: 300; }
</style>
</head>
<body>
<main class="flyer">
  <div class="scene-photo" role="img" aria-label="Tropical sky with palm tree fronds over a green cricket field"></div>
  <div class="player-photo" role="img" aria-label="Teenage girl in cricket whites mid bowling action holding a red cricket ball"></div>

  <header class="headline">
    <p class="eoi">Expressions of interest</p>
    <p class="tour">Cricket Tour Of <em>Sri Lanka</em></p>
    <p class="ages">For Girls Aged 14-18</p>
  </header>

  <section class="duration">
    <span class="count">10</span>
    <span class="label">Days Tour</span>
    <span class="dates">July 4th to 14th 2018</span>
  </section>
  <p class="grounds">First Class Grounds</p>

  <svg class="flag" viewBox="0 0 304 158" aria-label="Flag of Sri Lanka">
    <rect width="304" height="158" fill="var(--flag-gold)"/>
    <rect x="12" y="12" width="44" height="134" fill="var(--flag-green)"/>
    <rect x="56" y="12" width="44" height="134" fill="var(--flag-orange)"/>
    <rect x="122" y="12" width="170" height="134" fill="var(--flag-maroon)"/>
    <rect x="160" y="38" width="96" height="82" rx="8" fill="var(--flag-gold)" opacity=".9" role="img" aria-label="Golden lion holding a sword"/>
  </svg>

  <div class="brand">
    <span class="mark"></span><span class="name">Halvey Athletics</span>
  </div>

  <p class="coaches">Level 3 Coaches with International Experience</p>
  <p class="contact">Contact : boyd@halveyathletics.com.au</p>
</main>
</body>
</html>
```